business card design for luxurious real estate brand

using the attached logo, i am looking for a 2-sided business card design. the back should be the gold logo on black background. the front needs to include: gold logo, name, phone, email, and website

Industry/Entity Type

real estate

Contact Information for Business Card

logo, name, email, phone, website

Font styles to use
Sans Serif

```html
<!DOCTYPE html>
<html lang="en">
<head>
<meta charset="UTF-8">
<title>Casa Verano – Business Card</title>
<link href="https://fonts.googleapis.com/css2?family=Montserrat:wght@400;500;700&display=swap" rel="stylesheet">
<style>
  :root {
    --backdrop: #2a2a2c;
    --card: #1b1b1c;
    --gold: #d4a72c;
    --gold-soft: #c99a25;
  }
  * { margin: 0; padding: 0; box-sizing: border-box; }
  html, body {
    width: 1200px; height: 800px; overflow: hidden;
    background: var(--backdrop);
    font-family: "Montserrat", sans-serif;
  }
  .canvas {
    width: 1200px; height: 800px;
    display: flex; align-items: center; justify-content: center; gap: 40px;
  }
  .card {
    position: relative;
    width: 540px; height: 309px;
    background: var(--card);
    border-bottom: 3px solid var(--gold);
    box-shadow: 0 18px 40px rgba(0,0,0,0.45);
    color: var(--gold);
  }
  /* Front */
  .brand-mark {
    position: absolute; top: 34px; right: 38px;
    display: flex; align-items: center; gap: 8px;
    font-weight: 500; font-size: 13px; letter-spacing: 3px; text-transform: uppercase;
  }
  .brand-mark .dot { width: 8px; height: 8px; background: var(--gold); }
  .identity {
    position: absolute; left: 0; top: 150px; width: 262px;
    text-align: right; padding-right: 18px;
  }
  .identity .name { font-weight: 700; font-size: 22px; letter-spacing: 0.5px; }
  .identity .role { font-weight: 400; font-size: 13px; margin-top: 4px; color: var(--gold-soft); letter-spacing: 0.5px; }
  .divider {
    position: absolute; left: 262px; top: 138px; width: 1.5px; height: 62px;
    background: var(--gold);
  }
  .contacts {
    position: absolute; left: 282px; top: 138px;
    list-style: none; font-size: 12.5px; font-weight: 400;
  }
  .contacts li { display: flex; align-items: center; gap: 8px; height: 21px; }
  .contacts svg { width: 11px; height: 11px; fill: var(--gold); flex: none; }
  /* Back */
  .back { display: flex; align-items: center; justify-content: center; }
  .back .brand-mark {
    position: static; gap: 14px;
    font-size: 30px; letter-spacing: 9px;
  }
  .back .brand-mark .dot { width: 16px; height: 16px; }
</style>
</head>
<body>
<main class="canvas">
  <section class="card front" aria-label="Card front">
    <div class="brand-mark"><span class="dot"></span>Casa Verano</div>
    <div class="identity">
      <p class="name">Daniel Reyes</p>
      <p class="role">CEO &amp; Founder</p>
    </div>
    <div class="divider"></div>
    <ul class="contacts">
      <li>
        <svg viewBox="0 0 24 24" aria-hidden="true"><path d="M6.6 10.8a15.1 15.1 0 0 0 6.6 6.6l2.2-2.2a1 1 0 0 1 1-.25 11.4 11.4 0 0 0 3.6.57 1 1 0 0 1 1 1V20a1 1 0 0 1-1 1A17 17 0 0 1 3 4a1 1 0 0 1 1-1h3.5a1 1 0 0 1 1 1c0 1.25.2 2.45.57 3.57a1 1 0 0 1-.25 1z"/></svg>
        (555) 010-2040
      </li>
      <li>
        <svg viewBox="0 0 24 24" aria-hidden="true"><path d="M2 5h20v14H2zM3.5 6.5 12 13l8.5-6.5z" fill-rule="evenodd"/></svg>
        hello@casaverano.com
      </li>
      <li>
        <svg viewBox="0 0 24 24" aria-hidden="true"><path d="M12 2a10 10 0 1 0 0 20 10 10 0 0 0 0-20zm0 2.2c1 1.2 1.8 3 2.1 5H9.9c.3-2 1.1-3.8 2.1-5zM4.3 11h3.5c0 .7 0 1.3.1 2H4.3a7.9 7.9 0 0 1 0-2zm5.6 2c-.1-.7-.1-1.3 0-2h4.2c.1.7.1 1.3 0 2zm6.3 0c.1-.7.1-1.3.1-2h3.5a7.9 7.9 0 0 1 0 2zM12 19.8c-1-1.2-1.8-3-2.1-5h4.2c-.3 2-1.1 3.8-2.1 5z"/></svg>
        casaverano.com
      </li>
    </ul>
  </section>

  <section class="card back" aria-label="Card back">
    <div class="brand-mark"><span class="dot"></span>Casa Verano</div>
  </section>
</main>
</body>
</html>
```